Verdalunex webpage design

We are offering eco/sustainable theme vacations and make them bookable via our site. Our reference site is www.hovkalume.com. We want something similar but with a bit more creativity and elegant design. In our colors, which would depend on our logo colors.

NB: WE ARE NOT ASKING FOR A FULL BLOWN SITE. WE NEED 2 PAGE DESIGN FOR THE FIRST IMPRESSION. AFTER THAT WE CREATE A BUDGET FOR COMPLETION OF THE PROJECT.

Target Market(s)

Eco/Sustainable tourism.

Industry/Entity Type

Tourism

Coding

Coded - Design and coding required

Number of Pages Required

2 page

Requirements
Must have
• Reference site is hovkalume.com. But be creative and design something a bit different and more beautiful.
• NB: WE ARE NOT ASKING FOR A FULL BLOWN SITE. WE NEED 2 PAGE DESIGN FOR THE FIRST IMPRESSION. AFTER THAT WE CREATE A BUDGET FOR COMPLETION OF THE PROJECT.
• Please see our logo.

```html
<!DOCTYPE html>
<html lang="en">
<head>
<meta charset="utf-8">
<title>Verdalunex – Unforgettable travel experiences</title>
<link href="https://fonts.googleapis.com/css2?family=Lato:wght@400;700&display=swap" rel="stylesheet">
<style>
:root{
  --green:#1fc28f;
  --green-dark:#17a87b;
  --ink:#333a40;
  --muted:#8a9098;
  --line:#e3e5e8;
  --page:#f4f4f5;
  --white:#ffffff;
  --footer:#f7f7f8;
}
*{box-sizing:border-box;margin:0;padding:0}
html,body{width:691px;height:1200px;overflow:hidden}
body{font-family:"Lato",sans-serif;color:var(--ink);background:var(--white);position:relative}
a{color:inherit;text-decoration:none}

.site-header{height:20px;display:flex;align-items:center;padding:0 143px 0 144px;justify-content:space-between;background:var(--white)}
.brand{color:var(--green);font-weight:700;font-size:8px}
.top-nav{display:flex;align-items:center;gap:10px;font-size:4.6px;color:var(--ink)}
.top-nav .fav{color:var(--ink)}
.top-nav .fav span{color:var(--green)}
.btn{display:inline-flex;align-items:center;justify-content:center;background:var(--green);color:var(--white);font-weight:700;border-radius:1.5px}
.top-nav .btn{width:39px;height:12px;font-size:5px}

.hero{position:relative;height:230px;background:linear-gradient(180deg,#8db7d6 0%,#a9c8df 35%,#6f95b3 55%,#c8dbe8 72%,#9fb9cd 100%);text-align:center;color:var(--white)}
.hero h1{position:absolute;top:92px;left:0;right:0;font-size:17px;font-weight:700;text-shadow:0 1px 3px rgba(0,0,0,.35)}
.hero .tagline{position:absolute;top:111px;left:50%;transform:translateX(-50%);background:var(--green);font-size:6px;padding:1px 3px;white-space:nowrap}
.search{position:absolute;top:157px;left:180px;width:332px;height:21px;background:var(--white);border-radius:1.5px;display:flex;text-align:left;color:var(--ink)}
.search .field{flex:1;padding:3px 7px;border-right:1px solid var(--line)}
.search .field:last-child{border-right:0}
.search .label{font-size:3.6px;font-weight:700;letter-spacing:.2px;text-transform:uppercase}
.search .value{font-size:6px;color:var(--muted);margin-top:2px;display:flex;align-items:center;gap:2px}
.search svg{width:5px;height:5px}

.listing{background:var(--page);height:712px;position:relative}
.filters{position:absolute;left:146px;top:17px;width:93px}
.panel{background:var(--white);margin-bottom:13px;padding:0 0 5px}
.panel h3{font-size:5px;font-weight:700;text-transform:uppercase;padding:4px 5px 3px;border-bottom:1px solid var(--line);margin-bottom:4px;letter-spacing:.2px}
.opt{display:flex;justify-content:space-between;align-items:center;font-size:4.8px;color:var(--muted);padding:0 5px;height:11px}
.opt.tall{height:auto;padding-top:1px;padding-bottom:4px;align-items:flex-start;line-height:1.15}
.chev{width:3px;height:3px;border-right:.8px solid var(--green);border-bottom:.8px solid var(--green);transform:rotate(45deg);margin-top:-2px;margin-right:1px}
.radio{width:4.5px;height:4.5px;border:.7px solid #b7bcc2;border-radius:50%;flex:none}
.radio.on{border-color:var(--green);background:radial-gradient(circle,var(--green) 45%,transparent 50%)}
.check{width:5px;height:5px;border:.7px solid #b7bcc2;border-radius:1px;flex:none;position:relative}
.check.on{background:var(--green);border-color:var(--green)}
.check.on::after{content:"";position:absolute;left:1.4px;top:.4px;width:1.2px;height:2.4px;border-right:.7px solid #fff;border-bottom:.7px solid #fff;transform:rotate(45deg)}
.more{font-size:4.4px;color:var(--green);padding:1px 5px 4px}
.date-btn{margin:0 5px 3px;height:13px;border:1px solid var(--line);border-radius:1.5px;font-size:4.4px;display:flex;align-items:center;justify-content:center;gap:3px;color:var(--ink)}
.date-btn i{width:4px;height:4px;background:var(--green);opacity:.6;display:block}

.results{position:absolute;left:247px;top:17px;width:294px}
.sort{font-size:5px;height:9px;color:var(--ink)}
.sort b{font-weight:700}
.card{display:flex;background:var(--white);height:86px;margin-bottom:10px}
.card .photo{width:99px;flex:none}
.card .info{flex:1;padding:9px 10px 6px;position:relative;border-right:1px solid var(--line)}
.card h2{font-size:6px;font-weight:400;line-height:1.25;width:105px}
.features{position:absolute;left:10px;bottom:8px;font-size:4px;color:var(--muted);line-height:8.2px}
.features li{list-style:none;display:flex;align-items:center;gap:2px}
.features li::before{content:"";width:3.5px;height:3px;border:.6px solid var(--muted);border-radius:.5px}
.card .price{width:67px;flex:none;padding:6px 5px 0 7px;font-size:4px;color:var(--muted)}
.stars{display:flex;gap:.6px;height:7px}
.stars svg{width:7px;height:7px}
.from{margin-top:11px}
.amount{font-size:5.5px;font-weight:700;color:var(--ink)}
.for{margin-top:9px;line-height:6.5px}
.price .btn{width:56px;height:13px;font-size:4.8px;margin-top:4px}

.reviews{height:112px;text-align:center;padding-top:18px;background:var(--white)}
.reviews h2{font-size:9px;font-weight:400;color:#4a5057}
.reviews h2 b{font-weight:700;color:var(--ink)}
.review-row{display:flex;justify-content:center;gap:22px;margin-top:14px;text-align:left}
.review{display:flex;gap:4px;width:157px}
.avatar{width:34px;height:34px;border-radius:50%;flex:none;background:radial-gradient(circle at 50% 45%,#c9b3a0,#6d5a4b);margin-top:7px}
.review h4{font-size:5.6px;font-weight:700;margin-bottom:4px}
.review p{font-size:4px;color:var(--muted);line-height:1.35}
.review .who{font-size:4.6px;font-weight:700;color:var(--ink);margin-top:7px}
.review .when{font-size:3.8px;color:var(--muted)}

.site-footer{border-top:2px solid var(--line);background:var(--white);height:108px;display:flex;padding:12px 0 0 144px}
.col{width:87px}
.col.wide{width:129px}
.col.blog{width:129px}
.col h5{font-size:6px;font-weight:700;margin-bottom:7px}
.col li{list-style:none;font-size:4.6px;color:var(--muted);line-height:10px}
.col li.two{line-height:5.4px;margin:2px 0 3px}
.newsletter p{font-size:4.6px;color:var(--muted);line-height:1.2;width:88px}
.newsletter .email{width:86px;height:15px;border:1px solid #c9cdd2;margin-top:5px;font-size:4.6px;color:var(--muted);padding:4px 5px}
.newsletter .btn{width:86px;height:13px;font-size:4.6px;margin-top:4px}
.copyright{height:18px;background:var(--footer);font-size:5px;color:#5d636a;text-align:center;line-height:18px}
</style>
</head>
<body>

<header class="site-header">
  <a class="brand" href="#">Verdalunex</a>
  <nav class="top-nav">
    <span>US$ <span style="color:var(--green)">&#8964;</span></span>
    <span class="fav"><span>&#9825;</span> Favorites (0)</span>
    <span>Partners</span>
    <span>Log in</span>
    <a class="btn" href="#">Sign Up</a>
  </nav>
</header>

<section class="hero" role="img" aria-label="Family walking hand in hand along a beach as waves roll in">
  <h1>Unforgettable travel experiences</h1>
  <p class="tagline">A world of unique holidays, organized by passionate experts</p>
  <form class="search">
    <div class="field"><div class="label">Destination</div><div class="value"><svg viewBox="0 0 10 10"><path d="M5 1a3 3 0 0 1 3 3c0 2-3 5-3 5S2 6 2 4a3 3 0 0 1 3-3z" fill="none" stroke="#1fc28f"/></svg>Any destination</div></div>
    <div class="field"><div class="label">Duration &amp; arrival</div><div class="value"><svg viewBox="0 0 10 10"><rect x="1" y="2" width="8" height="7" fill="none" stroke="#1fc28f"/><path d="M1 4h8" stroke="#1fc28f"/></svg>Select duration or date</div></div>
    <div class="field"><div class="label">Activity type</div><div class="value"><svg viewBox="0 0 10 10"><path d="M5 1l1.2 2.6 2.8.3-2.1 1.9.6 2.8L5 7.2 2.5 8.6l.6-2.8L1 3.9l2.8-.3z" fill="none" stroke="#1fc28f" stroke-width=".8"/></svg>Any category</div></div>
  </form>
</section>

<main class="listing">
  <aside class="filters">
    <section class="panel">
      <h3>Destinations</h3>
      <div class="opt">Europe<span class="chev"></span></div>
      <div class="opt">Asia &amp; Oceania<span class="chev"></span></div>
      <div class="opt">Africa &amp; the Middle East<span class="chev"></span></div>
      <div class="opt">The Americas &amp; Caribbean<span class="chev"></span></div>
    </section>
    <section class="panel">
      <h3>Arrival date</h3>
      <div class="opt">2019 May (10433)<span class="radio"></span></div>
      <div class="opt">2019 June (11282)<span class="radio"></span></div>
      <div class="opt">2019 July (10531)<span class="radio on"></span></div>
      <div class="opt">2019 August (10245)<span class="radio"></span></div>
      <div class="opt">2019 September (10536)<span class="radio"></span></div>
      <div class="more">Show more</div>
      <div class="date-btn"><i></i>Select a specific date</div>
    </section>
    <section class="panel">
      <h3>Duration</h3>
      <div class="opt">2 days (787)<span class="check"></span></div>
      <div class="opt">From 3 to 7 days (8526)<span class="check"></span></div>
      <div class="opt">From 1 to 2 weeks (7036)<span class="check"></span></div>
      <div class="opt">More than 2 weeks (1884)<span class="check on"></span></div>
    </section>
    <section class="panel">
      <h3>Airport transfer</h3>
      <div class="opt tall">Airport transfer included<br><br>(5136)<span class="check"></span></div>
      <div class="opt tall">Airport transfer available<br><br>(2767)<span class="check on"></span></div>
    </section>
    <section class="panel">
      <h3>Categories</h3>
      <div class="opt">Accommodation type<span class="chev"></span></div>
      <div class="opt">Activity<span class="chev"></span></div>
      <div class="opt">Audience<span class="chev"></span></div>
      <div class="opt">Budget<span class="chev"></span></div>
      <div class="opt">Duration<span class="chev"></span></div>
      <div class="opt">Experience level<span class="chev"></span></div>
      <div class="opt">Experience Types<span class="chev"></span></div>
      <div class="opt">Focus/Atmosphere<span class="chev"></span></div>
      <div class="opt">Food<span class="chev"></span></div>
      <div class="opt">Intensity Level<span class="chev"></span></div>
      <div class="opt">Location<span class="chev"></span></div>
      <div class="opt">Special occasions<span class="chev"></span></div>
      <div class="opt">Time periods<span class="chev"></span></div>
    </section>
    <section class="panel">
      <h3>Price per trip</h3>
      <div class="opt">From US$0 to US$112 (299)<span class="check"></span></div>
      <div class="opt tall">From US$112 to US$336<br>(1440)<span class="check"></span></div>
      <div class="opt tall">From US$336 to US$1,008<br>(6523)<span class="check"></span></div>
      <div class="opt">More than US$1,008 (8364)<span class="check on"></span></div>
    </section>
  </aside>

  <section class="results">
    <div class="sort"><b>SORT BY:</b> Recommended</div>

    <article class="card">
      <div class="photo" role="img" aria-label="Bright living room with grey sofa and wooden floor" style="background:linear-gradient(160deg,#e9e4dc,#a99c8b 60%,#6d5f4f)"></div>
      <div class="info"><h2>13 Days Family Culinary Vacation in Hanoi, Vietnam</h2>
        <ul class="features"><li>Flexible cancellation policy</li><li>Airport transfer included</li><li>All meals included</li></ul></div>
      <div class="price"><div class="stars"><svg viewBox="0 0 10 10"><path d="M5 .8l1.3 2.8 3 .3-2.3 2 .7 3L5 7.3 2.3 8.9l.7-3L.7 3.9l3-.3z" fill="none" stroke="#1fc28f" stroke-width=".7"/></svg><svg viewBox="0 0 10 10"><path d="M5 .8l1.3 2.8 3 .3-2.3 2 .7 3L5 7.3 2.3 8.9l.7-3L.7 3.9l3-.3z" fill="none" stroke="#1fc28f" stroke-width=".7"/></svg><svg viewBox="0 0 10 10"><path d="M5 .8l1.3 2.8 3 .3-2.3 2 .7 3L5 7.3 2.3 8.9l.7-3L.7 3.9l3-.3z" fill="none" stroke="#1fc28f" stroke-width=".7"/></svg><svg viewBox="0 0 10 10"><path d="M5 .8l1.3 2.8 3 .3-2.3 2 .7 3L5 7.3 2.3 8.9l.7-3L.7 3.9l3-.3z" fill="none" stroke="#1fc28f" stroke-width=".7"/></svg><svg viewBox="0 0 10 10"><path d="M5 .8l1.3 2.8 3 .3-2.3 2 .7 3L5 7.3 2.3 8.9l.7-3L.7 3.9l3-.3z" fill="none" stroke="#1fc28f" stroke-width=".7"/></svg></div>
        <div class="from">from</div><div class="amount">US$1,145</div>
        <div class="for">Price for:<br>&#9675; 1 person<br>&#9638; 13 days / 12 nights</div>
        <a class="btn" href="#">See Details</a></div>
    </article>

    <article class="card">
      <div class="photo" role="img" aria-label="Attic bedroom with wooden ceiling and round window" style="background:linear-gradient(160deg,#5a3b27,#9a6a47 50%,#d9cfc4)"></div>
      <div class="info"><h2>13 Days Family Culinary Vacation in Hanoi, Vietnam</h2>
        <ul class="features"><li>Flexible cancellation policy</li><li>Airport transfer included</li><li>All meals included</li></ul></div>
      <div class="price"><div class="stars"><svg viewBox="0 0 10 10"><path d="M5 .8l1.3 2.8 3 .3-2.3 2 .7 3L5 7.3 2.3 8.9l.7-3L.7 3.9l3-.3z" fill="none" stroke="#1fc28f" stroke-width=".7"/></svg><svg viewBox="0 0 10 10"><path d="M5 .8l1.3 2.8 3 .3-2.3 2 .7 3L5 7.3 2.3 8.9l.7-3L.7 3.9l3-.3z" fill="none" stroke="#1fc28f" stroke-width=".7"/></svg><svg viewBox="0 0 10 10"><path d="M5 .8l1.3 2.8 3 .3-2.3 2 .7 3L5 7.3 2.3 8.9l.7-3L.7 3.9l3-.3z" fill="none" stroke="#1fc28f" stroke-width=".7"/></svg><svg viewBox="0 0 10 10"><path d="M5 .8l1.3 2.8 3 .3-2.3 2 .7 3L5 7.3 2.3 8.9l.7-3L.7 3.9l3-.3z" fill="none" stroke="#1fc28f" stroke-width=".7"/></svg><svg viewBox="0 0 10 10"><path d="M5 .8l1.3 2.8 3 .3-2.3 2 .7 3L5 7.3 2.3 8.9l.7-3L.7 3.9l3-.3z" fill="none" stroke="#1fc28f" stroke-width=".7"/></svg></div>
        <div class="from">from</div><div class="amount">US$1,145</div>
        <div class="for">Price for:<br>&#9675; 1 person<br>&#9638; 13 days / 12 nights</div>
        <a class="btn" href="#">See Details</a></div>
    </article>

    <article class="card">
      <div class="photo" role="img" aria-label="Modern open interior with floating staircase and plants" style="background:linear-gradient(160deg,#f2f2f0,#c9c3ba 55%,#6b5443)"></div>
      <div class="info"><h2>13 Days Family Culinary Vacation in Hanoi, Vietnam</h2>
        <ul class="features"><li>Flexible cancellation policy</li><li>Airport transfer included</li><li>All meals included</li></ul></div>
      <div class="price"><div class="stars"><svg viewBox="0 0 10 10"><path d="M5 .8l1.3 2.8 3 .3-2.3 2 .7 3L5 7.3 2.3 8.9l.7-3L.7 3.9l3-.3z" fill="none" stroke="#1fc28f" stroke-width=".7"/></svg><svg viewBox="0 0 10 10"><path d="M5 .8l1.3 2.8 3 .3-2.3 2 .7 3L5 7.3 2.3 8.9l.7-3L.7 3.9l3-.3z" fill="none" stroke="#1fc28f" stroke-width=".7"/></svg><svg viewBox="0 0 10 10"><path d="M5 .8l1.3 2.8 3 .3-2.3 2 .7 3L5 7.3 2.3 8.9l.7-3L.7 3.9l3-.3z" fill="none" stroke="#1fc28f" stroke-width=".7"/></svg><svg viewBox="0 0 10 10"><path d="M5 .8l1.3 2.8 3 .3-2.3 2 .7 3L5 7.3 2.3 8.9l.7-3L.7 3.9l3-.3z" fill="none" stroke="#1fc28f" stroke-width=".7"/></svg><svg viewBox="0 0 10 10"><path d="M5 .8l1.3 2.8 3 .3-2.3 2 .7 3L5 7.3 2.3 8.9l.7-3L.7 3.9l3-.3z" fill="none" stroke="#1fc28f" stroke-width=".7"/></svg></div>
        <div class="from">from</div><div class="amount">US$1,145</div>
        <div class="for">Price for:<br>&#9675; 1 person<br>&#9638; 13 days / 12 nights</div>
        <a class="btn" href="#">See Details</a></div>
    </article>

    <article class="card">
      <div class="photo" role="img" aria-label="Neutral bedroom with grey headboard and white linen" style="background:linear-gradient(160deg,#8e8a85,#d6d2cc 55%,#4f4c49)"></div>
      <div class="info"><h2>13 Days Family Culinary Vacation in Hanoi, Vietnam</h2>
        <ul class="features"><li>Flexible cancellation policy</li><li>Airport transfer included</li><li>All meals included</li></ul></div>
      <div class="price"><div class="stars"><svg viewBox="0 0 10 10"><path d="M5 .8l1.3 2.8 3 .3-2.3 2 .7 3L5 7.3 2.3 8.9l.7-3L.7 3.9l3-.3z" fill="none" stroke="#1fc28f" stroke-width=".7"/></svg><svg viewBox="0 0 10 10"><path d="M5 .8l1.3 2.8 3 .3-2.3 2 .7 3L5 7.3 2.3 8.9l.7-3L.7 3.9l3-.3z" fill="none" stroke="#1fc28f" stroke-width=".7"/></svg><svg viewBox="0 0 10 10"><path d="M5 .8l1.3 2.8 3 .3-2.3 2 .7 3L5 7.3 2.3 8.9l.7-3L.7 3.9l3-.3z" fill="none" stroke="#1fc28f" stroke-width=".7"/></svg><svg viewBox="0 0 10 10"><path d="M5 .8l1.3 2.8 3 .3-2.3 2 .7 3L5 7.3 2.3 8.9l.7-3L.7 3.9l3-.3z" fill="none" stroke="#1fc28f" stroke-width=".7"/></svg><svg viewBox="0 0 10 10"><path d="M5 .8l1.3 2.8 3 .3-2.3 2 .7 3L5 7.3 2.3 8.9l.7-3L.7 3.9l3-.3z" fill="none" stroke="#1fc28f" stroke-width=".7"/></svg></div>
        <div class="from">from</div><div class="amount">US$1,145</div>
        <div class="for">Price for:<br>&#9675; 1 person<br>&#9638; 13 days / 12 nights</div>
        <a class="btn" href="#">See Details</a></div>
    </article>

    <article class="card">
      <div class="photo" role="img" aria-label="Warm bedroom with wooden headboard and blue bedspread" style="background:linear-gradient(160deg,#a7b6c0,#7a4a2c 50%,#3f6f86)"></div>
      <div class="info"><h2>13 Days Family Culinary Vacation in Hanoi, Vietnam</h2>
        <ul class="features"><li>Flexible cancellation policy</li><li>Airport transfer included</li><li>All meals included</li></ul></div>
      <div class="price"><div class="stars"><svg viewBox="0 0 10 10"><path d="M5 .8l1.3 2.8 3 .3-2.3 2 .7 3L5 7.3 2.3 8.9l.7-3L.7 3.9l3-.3z" fill="none" stroke="#1fc28f" stroke-width=".7"/></svg><svg viewBox="0 0 10 10"><path d="M5 .8l1.3 2.8 3 .3-2.3 2 .7 3L5 7.3 2.3 8.9l.7-3L.7 3.9l3-.3z" fill="none" stroke="#1fc28f" stroke-width=".7"/></svg><svg viewBox="0 0 10 10"><path d="M5 .8l1.3 2.8 3 .3-2.3 2 .7 3L5 7.3 2.3 8.9l.7-3L.7 3.9l3-.3z" fill="none" stroke="#1fc28f" stroke-width=".7"/></svg><svg viewBox="0 0 10 10"><path d="M5 .8l1.3 2.8 3 .3-2.3 2 .7 3L5 7.3 2.3 8.9l.7-3L.7 3.9l3-.3z" fill="none" stroke="#1fc28f" stroke-width=".7"/></svg><svg viewBox="0 0 10 10"><path d="M5 .8l1.3 2.8 3 .3-2.3 2 .7 3L5 7.3 2.3 8.9l.7-3L.7 3.9l3-.3z" fill="none" stroke="#1fc28f" stroke-width=".7"/></svg></div>
        <div class="from">from</div><div class="amount">US$1,145</div>
        <div class="for">Price for:<br>&#9675; 1 person<br>&#9638; 13 days / 12 nights</div>
        <a class="btn" href="#">See Details</a></div>
    </article>

    <article class="card">
      <div class="photo" role="img" aria-label="Minimal bedroom with sheer curtains and brown throw" style="background:linear-gradient(160deg,#e6e4e1,#bdb8b2 55%,#6e6256)"></div>
      <div class="info"><h2>13 Days Family Culinary Vacation in Hanoi, Vietnam</h2>
        <ul class="features"><li>Flexible cancellation policy</li><li>Airport transfer included</li><li>All meals included</li></ul></div>
      <div class="price"><div class="stars"><svg viewBox="0 0 10 10"><path d="M5 .8l1.3 2.8 3 .3-2.3 2 .7 3L5 7.3 2.3 8.9l.7-3L.7 3.9l3-.3z" fill="none" stroke="#1fc28f" stroke-width=".7"/></svg><svg viewBox="0 0 10 10"><path d="M5 .8l1.3 2.8 3 .3-2.3 2 .7 3L5 7.3 2.3 8.9l.7-3L.7 3.9l3-.3z" fill="none" stroke="#1fc28f" stroke-width=".7"/></svg><svg viewBox="0 0 10 10"><path d="M5 .8l1.3 2.8 3 .3-2.3 2 .7 3L5 7.3 2.3 8.9l.7-3L.7 3.9l3-.3z" fill="none" stroke="#1fc28f" stroke-width=".7"/></svg><svg viewBox="0 0 10 10"><path d="M5 .8l1.3 2.8 3 .3-2.3 2 .7 3L5 7.3 2.3 8.9l.7-3L.7 3.9l3-.3z" fill="none" stroke="#1fc28f" stroke-width=".7"/></svg><svg viewBox="0 0 10 10"><path d="M5 .8l1.3 2.8 3 .3-2.3 2 .7 3L5 7.3 2.3 8.9l.7-3L.7 3.9l3-.3z" fill="none" stroke="#1fc28f" stroke-width=".7"/></svg></div>
        <div class="from">from</div><div class="amount">US$1,145</div>
        <div class="for">Price for:<br>&#9675; 1 person<br>&#9638; 13 days / 12 nights</div>
        <a class="btn" href="#">See Details</a></div>
    </article>

    <article class="card">
      <div class="photo" role="img" aria-label="Cosy lounge with stone fireplace and chandelier" style="background:linear-gradient(160deg,#efe8df,#b9a993 50%,#4d4037)"></div>
      <div class="info"><h2>13 Days Family Culinary Vacation in Hanoi, Vietnam</h2>
        <ul class="features"><li>Flexible cancellation policy</li><li>Airport transfer included</li><li>All meals included</li></ul></div>
      <div class="price"><div class="stars"><svg viewBox="0 0 10 10"><path d="M5 .8l1.3 2.8 3 .3-2.3 2 .7 3L5 7.3 2.3 8.9l.7-3L.7 3.9l3-.3z" fill="none" stroke="#1fc28f" stroke-width=".7"/></svg><svg viewBox="0 0 10 10"><path d="M5 .8l1.3 2.8 3 .3-2.3 2 .7 3L5 7.3 2.3 8.9l.7-3L.7 3.9l3-.3z" fill="none" stroke="#1fc28f" stroke-width=".7"/></svg><svg viewBox="0 0 10 10"><path d="M5 .8l1.3 2.8 3 .3-2.3 2 .7 3L5 7.3 2.3 8.9l.7-3L.7 3.9l3-.3z" fill="none" stroke="#1fc28f" stroke-width=".7"/></svg><svg viewBox="0 0 10 10"><path d="M5 .8l1.3 2.8 3 .3-2.3 2 .7 3L5 7.3 2.3 8.9l.7-3L.7 3.9l3-.3z" fill="none" stroke="#1fc28f" stroke-width=".7"/></svg><svg viewBox="0 0 10 10"><path d="M5 .8l1.3 2.8 3 .3-2.3 2 .7 3L5 7.3 2.3 8.9l.7-3L.7 3.9l3-.3z" fill="none" stroke="#1fc28f" stroke-width=".7"/></svg></div>
        <div class="from">from</div><div class="amount">US$1,145</div>
        <div class="for">Price for:<br>&#9675; 1 person<br>&#9638; 13 days / 12 nights</div>
        <a class="btn" href="#">See Details</a></div>
    </article>
  </section>
</main>

<section class="reviews">
  <h2>Reviews from <b>RATEWELL</b></h2>
  <div class="review-row">
    <div class="review">
      <div class="avatar" role="img" aria-label="Reviewer portrait"></div>
      <div><h4>You can easily compare the retreats</h4>
        <p>You can easily compare the retreats, they're all the info you need about every retreat.</p>
        <div class="who">Ana Ruel</div><div class="when">Tuesday, November 27, 2018</div></div>
    </div>
    <div class="review">
      <div class="avatar" role="img" aria-label="Reviewer portrait" style="background:radial-gradient(circle at 50% 45%,#e2c8a6,#8a6a45)"></div>
      <div><h4>Great website</h4>
        <p>You can easily compare the retreats, they're all the info you need about every retreat.</p>
        <div class="who">Lena V.</div><div class="when">Tuesday, July 17, 2018</div></div>
    </div>
  </div>
</section>

<footer class="site-footer">
  <div class="col"><h5>Hovkalume</h5>
    <ul><li>About Hovkalume</li><li>Add / Manage your business</li><li>Become An Affiliate</li><li>Newsletter Sign Up</li><li>Site Map</li><li>Work with us</li></ul></div>
  <div class="col blog"><h5>Recent Blog Articles</h5>
    <ul><li>Quirky &amp; Bizarre Christmas Traditions</li><li>The Best Ski &amp; Snowboard Festivals</li><li>Europe's Best Christmas Markets</li><li class="two">A Hipster's Guide to London: Where to<br>Eat, Drink, and Sightsee in The Capital</li><li>A Guide to Authentic Mexican Food</li></ul></div>
  <div class="col wide" style="width:102px"><h5>Our Websites</h5>
    <ul><li>StayMartialArts</li><li>StayCulinaryTrips</li><li>StayYogaEscapes</li><li>StayCyclingTours</li><li>StaySurfHavens</li><li>StayRidingTrips</li></ul></div>
  <div class="col newsletter"><h5>Newsletter Sign Up</h5>
    <p>Don't miss our special promotions, exclusive offers, new destinations and inspirational stories!</p>
    <div class="email">Enter Your Email</div>
    <a class="btn" href="#">Sign up for our newsletter</a></div>
</footer>
<div class="copyright">Copyright © 2019 Verdalunex</div>

</body>
</html>
```